Velvet Basin Suites, a portable luxury restroom trailer company needs a landing page

We need a landing page for a luxury portable restroom trailer company. This should be modern, and simple - use any combination of Pantone colors: Warm Gray 1C, Black 7C, 7529c, 873C, 8003C

We rent these trailers for special events like weddings, private parties, festivals, family reunions, team building, wine tastings, beer tastings, food truck round-ups, etc.

An idea of the landing page is in the files below. Please use stock photography and placeholder text for now. The winning design will be given final content.

Requirements
Must have
• Multiple "Get Quote" buttons or a place for them to type in type of rental, how many people etc

```html
<!DOCTYPE html>
<html lang="en">
<head>
<meta charset="utf-8">
<title>Velvet Basin Suites — Luxury Restroom Trailers</title>
<link href="https://fonts.googleapis.com/css2?family=Poppins:wght@300;400;500;600;700;800&family=Roboto:wght@400;500&display=swap" rel="stylesheet">
<style>
:root{
  --warm-gray:#d7d2cb;
  --taupe:#c5b9ac;
  --black:#2b2b2b;
  --ink:#222;
  --body:#555;
  --gold:#a5825a;
  --brown:#735a3c;
  --hero:#a98866;
  --white:#fff;
}
*{margin:0;padding:0;box-sizing:border-box}
html,body{width:1200px;height:3715px;overflow:hidden}
body{position:relative;background:var(--white);font-family:"Roboto",sans-serif;color:var(--ink)}
.abs{position:absolute}
.ph{position:absolute;display:block}

/* hero */
.hero{position:absolute;left:0;top:0;width:1200px;height:639px;background:linear-gradient(90deg,#b9997a 0%,#a98866 45%,#9a7a5b 100%);overflow:hidden}
.hero-bg{left:0;top:0;width:1200px;height:639px;background:linear-gradient(120deg,rgba(210,190,165,.35),rgba(120,95,70,.25))}
.brand{position:absolute;display:flex;flex-direction:column;align-items:center;gap:6px}
.brand .mark{width:46px;height:46px;border-radius:50%;border:3px solid currentColor}
.brand .name{font-family:"Poppins",sans-serif;font-weight:400;font-size:15px;letter-spacing:.5px;white-space:nowrap}
.hero .brand{left:104px;top:8px;color:var(--white)}
.nav{position:absolute;top:28px;display:flex;font-family:"Poppins",sans-serif;font-weight:300;font-size:15px;color:var(--white)}
.nav a{position:absolute;color:inherit;text-decoration:none;white-space:nowrap}
.search{position:absolute;left:812px;top:22px;width:125px;height:30px;border-bottom:1px solid rgba(255,255,255,.7);color:var(--white);font-family:"Poppins",sans-serif;font-weight:300;font-size:14px}
.search svg{position:absolute;right:4px;top:4px}
.btn{display:flex;align-items:center;justify-content:center;background:var(--black);color:var(--white);font-family:"Poppins",sans-serif;font-weight:600;border-radius:6px;text-decoration:none}
.login{position:absolute;left:973px;top:14px;width:111px;height:49px;font-size:14px}
.welcome{left:110px;top:170px;font-family:"Poppins",sans-serif;font-weight:300;font-size:46px;color:var(--white);letter-spacing:.5px}
.hero-title{left:106px;top:234px;font-family:"Poppins",sans-serif;font-weight:800;font-size:68px;line-height:92px;color:var(--white);text-transform:uppercase}
.hero-text{left:110px;top:436px;width:450px;font-size:14px;line-height:24px;color:var(--white)}
.quote{position:absolute;left:111px;top:506px;width:154px;height:52px;font-size:14px}
.tile{position:absolute;border:3px solid #cfcfcf;box-shadow:0 2px 6px rgba(0,0,0,.25)}

/* headings */
.eyebrow{position:absolute;left:0;width:1200px;text-align:center;font-family:"Poppins",sans-serif;font-size:21px;color:var(--ink)}
.section-title{position:absolute;left:0;width:1200px;text-align:center;font-family:"Poppins",sans-serif;font-weight:600;font-size:30px;color:var(--ink)}
.rule{position:absolute;left:560px;top:811px;width:80px;height:2px;background:var(--gold)}

/* events */
.event{position:absolute;width:476px;height:232px;background:var(--white);box-shadow:0 2px 10px rgba(0,0,0,.12);border-radius:4px;overflow:hidden}
.event .ph{left:0;top:0;width:213px;height:232px}
.event .body{position:absolute;left:236px;top:28px;width:220px}
.event h3{font-family:"Poppins",sans-serif;font-weight:400;font-size:18px;color:var(--ink);margin-bottom:14px}
.event p{font-family:"Poppins",sans-serif;font-size:14px;line-height:26px;color:var(--body);text-align:justify}
.event a{display:block;margin-top:12px;font-family:"Poppins",sans-serif;font-weight:500;font-size:15px;color:var(--gold);text-decoration:none}
.more{position:absolute;left:523px;top:1390px;width:158px;height:51px;font-size:14px}

/* about */
.about{position:absolute;left:0;top:1527px;width:1200px;height:513px;background:linear-gradient(90deg,#2e3a26 0%,#3d4630 25%,#6f6c66 45%,#8a8782 65%,#161616 85%,#0c0c0c 100%)}
.about-card{position:absolute;left:111px;top:88px;width:397px;height:361px;border-radius:14px;background:linear-gradient(100deg,#9c9c9c 0%,#f4f4f4 35%,#e4e4e4 60%,#8d8d8d 100%);box-shadow:-6px 8px 0 rgba(255,255,255,.25);text-align:center;padding:30px 24px}
.about-card h2{font-family:"Poppins",sans-serif;font-weight:500;font-size:28px;line-height:43px;color:var(--ink)}
.about-card p{margin-top:14px;font-family:"Poppins",sans-serif;font-size:14px;line-height:26px;color:#333}
.learn{margin:22px auto 0;width:140px;height:51px;font-size:14px}

/* products */
.lead{position:absolute;left:330px;top:2176px;width:540px;text-align:center;font-family:"Poppins",sans-serif;font-size:14px;line-height:26px;color:#333}
.product{position:absolute;top:2268px;width:309px;height:354px;background:var(--white);border-radius:12px;box-shadow:0 3px 12px rgba(0,0,0,.14);overflow:hidden}
.product .ph{left:0;top:0;width:309px;height:179px}
.product h3{position:absolute;left:21px;top:201px;width:270px;font-family:"Roboto",sans-serif;font-weight:500;font-size:18px;line-height:22px;color:#223}
.product p{position:absolute;left:21px;top:264px;width:260px;font-family:"Poppins",sans-serif;font-size:14px;line-height:22px;color:var(--body)}
.dots{position:absolute;left:21px;top:326px;display:flex;gap:6px}
.dots i{width:6px;height:6px;border-radius:50%;background:var(--gold);opacity:.8}

/* contact */
.contact{position:absolute;left:0;top:2708px;width:1200px;height:652px;background:var(--brown)}
.contact .kicker{position:absolute;left:0;top:64px;width:1200px;text-align:center;font-family:"Poppins",sans-serif;font-weight:600;font-size:13px;color:var(--white)}
.contact h2{position:absolute;left:0;top:88px;width:1200px;text-align:center;font-family:"Poppins",sans-serif;font-weight:600;font-size:30px;color:var(--white)}
.field{position:absolute;height:52px;background:var(--white);border-radius:5px;padding-left:15px;display:flex;align-items:center;font-family:"Roboto",sans-serif;font-size:13px;color:#666}
.field svg{position:absolute;right:16px;top:20px}
.submit{position:absolute;left:534px;top:547px;width:132px;height:43px;border:2px solid var(--white);border-radius:6px;color:var(--white);font-family:"Poppins",sans-serif;font-weight:600;font-size:14px;display:flex;align-items:center;justify-content:center}

/* footer */
.footer .brand{left:111px;top:3414px;color:#c79a3c}
.footer .brand .name{font-size:18px}
.social{position:absolute;top:3542px;width:37px;height:37px;border-radius:50%;background:#e4e2df}
.fhead{position:absolute;top:3437px;font-family:"Poppins",sans-serif;font-weight:500;font-size:21px;color:var(--ink)}
.flinks{position:absolute;top:3482px;list-style:none;font-family:"Poppins",sans-serif;font-size:14px;line-height:26px;color:#333}
.flinks li::before{content:"›";color:#999;margin-right:9px}
.finfo{position:absolute;left:839px;font-family:"Poppins",sans-serif;font-size:14px;line-height:26px;color:#333;padding-left:24px}
.finfo svg{position:absolute;left:0;top:6px}
.divider{position:absolute;left:111px;top:3643px;width:976px;height:1px;background:#ddd}
.legal{position:absolute;top:3662px;font-family:"Roboto",sans-serif;font-size:13px;color:#333}
.chat{position:absolute;left:1155px;top:3438px;width:46px;height:46px;border-radius:50%;background:#f1f1f1;box-shadow:0 1px 4px rgba(0,0,0,.25)}
</style>
</head>
<body>

<header class="hero">
  <div class="ph hero-bg" role="img" aria-label="Background photo of a white restroom trailer interior in warm light"></div>
  <div class="brand"><span class="mark"></span><span class="name">VELVET BASIN SUITES</span></div>
  <nav class="nav">
    <a style="left:379px">HOME</a>
    <a style="left:480px">EVENT</a>
    <a style="left:585px">PRODUCT</a>
    <a style="left:712px">CONTACT</a>
  </nav>
  <div class="search"><span style="position:absolute;top:2px">Search</span>
    <svg width="14" height="14" viewBox="0 0 14 14"><circle cx="6" cy="6" r="4.5" fill="none" stroke="#fff" stroke-width="2"/><line x1="9.5" y1="9.5" x2="13" y2="13" stroke="#fff" stroke-width="2"/></svg>
  </div>
  <a class="btn login">LOG IN</a>

  <div class="abs welcome">WELCOME TO</div>
  <h1 class="abs hero-title">Velvet Basin<br>Suites</h1>
  <p class="abs hero-text">Lorem ipsum dolor sit amet, consectetur adipiscing elit, sed do v incididunt ut labore et dolore magna aliqua.</p>
  <a class="btn quote">REQUEST QUOTE</a>

  <div class="tile" style="left:565px;top:75px;width:252px;height:252px;background:linear-gradient(135deg,#3a3836,#bdb7b0)" role="img" aria-label="Photo of a wedding couple celebrating"></div>
  <div class="tile" style="left:819px;top:121px;width:173px;height:167px;background:linear-gradient(135deg,#3b3531,#8b7a6c)" role="img" aria-label="Photo of guests embracing at a wedding"></div>
  <div class="tile" style="left:995px;top:89px;width:199px;height:159px;background:linear-gradient(160deg,#8fa1b3,#d7d3c8)" role="img" aria-label="Photo of a white restroom trailer parked outdoors"></div>
  <div class="tile" style="left:646px;top:265px;width:198px;height:150px;background:linear-gradient(180deg,#4f6b8a,#9aa29c)" role="img" aria-label="Photo of a trailer at a campsite"></div>
  <div class="tile" style="left:846px;top:291px;width:173px;height:141px;background:linear-gradient(180deg,#9fc2e0,#6f8a5b)" role="img" aria-label="Photo of trailers lined up under blue sky"></div>
  <div class="tile" style="left:1019px;top:252px;width:181px;height:125px;background:linear-gradient(135deg,#5a3e2b,#c49a72)" role="img" aria-label="Photo of friends laughing together"></div>
  <div class="tile" style="left:594px;top:421px;width:211px;height:216px;background:linear-gradient(180deg,#8e9fb0,#d9d9d6)" role="img" aria-label="Photo of a white food truck"></div>
  <div class="tile" style="left:808px;top:441px;width:176px;height:194px;background:linear-gradient(135deg,#3f4f6a,#c8a24a)" role="img" aria-label="Photo of friends celebrating at a party"></div>
  <div class="tile" style="left:985px;top:382px;width:215px;height:254px;background:linear-gradient(135deg,#6e4a34,#c79b78)" role="img" aria-label="Photo of guests toasting with wine"></div>
</header>

<main>
  <section class="events">
    <div class="eyebrow" style="top:729px">Our Events</div>
    <h2 class="section-title" style="top:760px">Sed ut perspiciatis unde omnis</h2>
    <div class="rule"></div>

    <article class="event" style="left:111px;top:867px">
      <div class="ph" style="background:linear-gradient(160deg,#5c7142,#2f63b5 55%,#3b3b3b)" role="img" aria-label="Photo of a blue portable toilet on a trailer"></div>
      <div class="body"><h3>WEDDINGS</h3><p>Lorem ipsum dolor sit amet, consectetur adipiscing elit, sed do eiusmod tempor incididunt eiusmod tempor incididunt</p><a>Read More</a></div>
    </article>
    <article class="event" style="left:611px;top:867px">
      <div class="ph" style="background:linear-gradient(160deg,#56693e,#2f7a56 55%,#444)" role="img" aria-label="Photo of green portable toilets on a truck"></div>
      <div class="body"><h3>PRIVATE PARTIES</h3><p>Lorem ipsum dolor sit amet, consectetur adipiscing elit, sed do eiusmod tempor incididunt eiusmod tempor incididunt</p><a>Read More</a></div>
    </article>
    <article class="event" style="left:111px;top:1123px">
      <div class="ph" style="background:linear-gradient(90deg,#4a5360,#8a95a4 50%,#3c4450)" role="img" aria-label="Photo of a silver restroom trailer with warm lights"></div>
      <div class="body"><h3>FESTIVALS</h3><p>Lorem ipsum dolor sit amet, consectetur adipiscing elit, sed do eiusmod tempor incididunt eiusmod tempor incididunt</p><a>Read More</a></div>
    </article>
    <article class="event" style="left:611px;top:1123px">
      <div class="ph" style="background:linear-gradient(160deg,#8b3a2e,#7a5a3e 55%,#3a3128)" role="img" aria-label="Photo of a wooden barrel-shaped restroom trailer"></div>
      <div class="body"><h3>FAMILY REUNIONS</h3><p>Lorem ipsum dolor sit amet, consectetur adipiscing elit, sed do eiusmod tempor incididunt eiusmod tempor incididunt</p><a>Read More</a></div>
    </article>

    <a class="btn more">SEE MORE BLOG</a>
  </section>

  <section class="about" role="img" aria-label="Background photo of a stainless steel restroom trailer at dusk">
    <div class="about-card">
      <h2>ABOUT VELVET<br>BASIN SUITES</h2>
      <p>Lorem ipsum dolor sit amet, consectetur adipiscing elit, sed do eiusmod tempor incididunt ut labore et dolore magna aliqua. Ut enim ad minim veniam, quis nostrud exercitation ullamco laboris nisi ut aliquip ex ea commodo consequat.</p>
      <a class="btn learn">LEARN MORE</a>
    </div>
  </section>

  <section class="products">
    <h2 class="section-title" style="top:2118px">Our Products</h2>
    <p class="lead">Lorem ipsum dolor sit amet, consectetur adipiscing elit, sed do eiusmod tempor incididunt ut labore et dolore magna aliqua.</p>

    <article class="product" style="left:111px">
      <div class="ph" style="background:linear-gradient(180deg,#6d5a4c,#c9c9c6 55%,#3a3a3a)" role="img" aria-label="Photo of a grey restroom trailer"></div>
      <h3>Sed ut perspiciatis unde omnis iste natus error sit</h3>
      <p>Lorem ipsum dolor sit amet, consectetur adipiscing elit, sed do</p>
      <div class="dots"><i></i><i></i><i></i></div>
    </article>
    <article class="product" style="left:446px">
      <div class="ph" style="background:linear-gradient(90deg,#9c9690,#ece8e2 50%,#7a4f3a)" role="img" aria-label="Photo of a trailer interior with shower"></div>
      <h3>Sed ut perspiciatis unde omnis iste natus error sit</h3>
      <p>Lorem ipsum dolor sit amet, consectetur adipiscing elit, sed do</p>
      <div class="dots"><i></i><i></i><i></i></div>
    </article>
    <article class="product" style="left:779px">
      <div class="ph" style="background:linear-gradient(180deg,#e6e6e6,#bdbdbd 60%,#8e8e8e)" role="img" aria-label="Photo of a row of white restroom trailers with steps"></div>
      <h3>Sed ut perspiciatis unde omnis iste natus error sit</h3>
      <p>Lorem ipsum dolor sit amet, consectetur adipiscing elit, sed do</p>
      <div class="dots"><i></i><i></i><i></i></div>
    </article>
  </section>

  <section class="contact">
    <div class="kicker">GET IN TOUCH</div>
    <h2>Contact us for a Quote</h2>
    <div class="field" style="left:314px;top:159px;width:280px">Name</div>
    <div class="field" style="left:604px;top:159px;width:281px">Email</div>
    <div class="field" style="left:314px;top:220px;width:571px;height:55px">Phone</div>
    <div class="field" style="left:314px;top:284px;width:280px">Type of Event?<svg width="12" height="8" viewBox="0 0 12 8"><path d="M1 1l5 5 5-5" fill="none" stroke="#777" stroke-width="1.5"/></svg></div>
    <div class="field" style="left:604px;top:284px;width:281px">How Many People?<svg width="12" height="8" viewBox="0 0 12 8"><path d="M1 1l5 5 5-5" fill="none" stroke="#777" stroke-width="1.5"/></svg></div>
    <div class="field" style="left:314px;top:348px;width:571px;height:54px">Type of Product Your Intersted in?<svg width="12" height="8" viewBox="0 0 12 8"><path d="M1 1l5 5 5-5" fill="none" stroke="#777" stroke-width="1.5"/></svg></div>
    <div class="field" style="left:314px;top:412px;width:280px">When do you need it?</div>
    <div class="field" style="left:604px;top:412px;width:281px">For how Long?</div>
    <div class="field" style="left:314px;top:475px;width:571px;height:54px">Where?</div>
    <a class="submit">SUBMIT NOW</a>
  </section>
</main>

<footer class="footer">
  <div class="brand"><span class="mark"></span><span class="name">VELVET BASIN SUITES</span></div>
  <span class="social" style="left:111px"></span>
  <span class="social" style="left:163px"></span>
  <span class="social" style="left:215px"></span>
  <span class="social" style="left:267px"></span>

  <h4 class="fhead" style="left:398px">QUICK LINK</h4>
  <ul class="flinks" style="left:398px"><li>Home</li><li>Event</li><li>Product</li><li>Contact</li></ul>

  <h4 class="fhead" style="left:626px">EVENTS</h4>
  <ul class="flinks" style="left:626px"><li>Weddings</li><li>Private Parties</li><li>Festivals</li><li>Family Reunions</li><li>Team Building</li></ul>

  <h4 class="fhead" style="left:839px">CONTACT US</h4>
  <div class="finfo" style="top:3484px;width:250px">
    <svg width="12" height="15" viewBox="0 0 12 15"><path d="M6 0a6 6 0 0 0-6 6c0 4.5 6 9 6 9s6-4.5 6-9a6 6 0 0 0-6-6z" fill="#222"/><circle cx="6" cy="6" r="2.2" fill="#fff"/></svg>
    Lorem ipsum dolor sit amet, consectetur adipiscing elit, sed
  </div>
  <div class="finfo" style="top:3549px">
    <svg width="13" height="13" viewBox="0 0 24 24"><path d="M6.6 10.8a15.1 15.1 0 0 0 6.6 6.6l2.2-2.2a1 1 0 0 1 1-.25 11.4 11.4 0 0 0 3.6.57 1 1 0 0 1 1 1V20a1 1 0 0 1-1 1A17 17 0 0 1 3 4a1 1 0 0 1 1-1h3.5a1 1 0 0 1 1 1c0 1.25.2 2.45.57 3.6a1 1 0 0 1-.25 1z" fill="#222"/></svg>
    +1 (555) 014 2290
  </div>
  <div class="finfo" style="top:3588px">
    <svg width="14" height="11" viewBox="0 0 14 11"><rect width="14" height="11" rx="1" fill="#222"/><path d="M1 1.5l6 4.5 6-4.5" fill="none" stroke="#fff" stroke-width="1.2"/></svg>
    hello@velvetbasinsuites.com
  </div>

  <div class="chat"><svg width="46" height="46" viewBox="0 0 46 46"><circle cx="15" cy="23" r="3" fill="#555"/><circle cx="23" cy="23" r="3" fill="#555"/><circle cx="31" cy="23" r="3" fill="#555"/></svg></div>

  <div class="divider"></div>
  <div class="legal" style="left:111px">©Copyrights 2022 Velvet Basin Suites</div>
  <div class="legal" style="left:877px">Privacy Policy | Terms &amp; condtions</div>
</footer>

</body>
</html>
```